Carrowfield Hotel

A Hotel (Pub) in Sydney CBD. Posters will be outside of Hotel informing People what is on in Hotel.
We will be Printing in A1 size.
CARROWFIELD HOTEL
Open 9am - 3am 7 Days
Monday - Thursday
Happy Hour
4pm - 6pm
Local Beer & Wine
Wednesday
Poker Night: Great $$$ Prizes
Everyday
Steak or Schniztels: Served with Mashed Potato & Salad or Chips & Salad - $8.50
Live Sport on the Big Screen
BISTRO
OPEN 7 DAYS 12- 9pm
Daily Blackboard Specials + Full Menu Inside
Best service in Town
Target Market(s)
Male or Female 18 to Seniors.Passing Trade.
Industry/Entity Type
Hotel
Look and feel
Each slider illustrates characteristics of the customer's brand and the style your logo design should communicate.

```html
<!DOCTYPE html>
<html lang="en">
<head>
<meta charset="utf-8">
<title>Carrowfield Hotel – What's On</title>
<link rel="stylesheet" href="https://fonts.googleapis.com/css2?family=Kaushan+Script&family=Bungee+Inline&family=Schoolbell&family=Alfa+Slab+One&family=Mystery+Quest&family=Roboto:wght@700;900&display=swap">
<style>
  :root {
    --purple-deep: #3b1470;
    --purple-mid: #6a2fb0;
    --purple-light: #9a5ad6;
    --maroon: rgba(122, 30, 78, 0.82);
    --sign-fill: #c23ad6;
    --sign-edge: #f2f2f2;
    --brown-ink: #5a2a14;
    --cream: #fff6ec;
    --pink-soft: #f2c6e6;
    --gold: #c8a13a;
    --yellow: #ffe21a;
    --badge-blue: #1f7fd8;
    --board: #1e1e1e;
    --board-frame: #c48a4a;
    --wood-dark: #4a2c14;
    --wood-light: #7a4e28;
    --silver: #d6d6d6;
    --white: #ffffff;
  }
  * { margin: 0; padding: 0; box-sizing: border-box; }
  html, body { width: 849px; height: 1200px; overflow: hidden; }
  body { background: var(--purple-deep); }
  .poster {
    position: relative; width: 849px; height: 1200px; overflow: hidden;
    background: radial-gradient(circle at 62% 46%, var(--purple-light) 0%, var(--purple-mid) 38%, var(--purple-deep) 100%);
    font-family: "Roboto", sans-serif;
  }
  .abs { position: absolute; white-space: nowrap; }

  .brand-panel { left: 0; top: 0; width: 425px; height: 200px; background: var(--maroon); }
  .brand-name { left: 30px; top: 62px; font-family: "Kaushan Script", cursive; font-size: 50px; color: var(--white); line-height: 1; }

  .open-sign { left: 485px; top: 18px; width: 364px; height: 280px; }

  .script-heading {
    font-family: "Kaushan Script", cursive; color: var(--cream);
    -webkit-text-stroke: 2px var(--brown-ink);
    text-shadow: 3px 3px 0 var(--brown-ink), 0 0 8px rgba(0,0,0,.35);
    line-height: 1;
  }
  .script-label {
    font-family: "Kaushan Script", cursive; color: var(--pink-soft);
    -webkit-text-stroke: 1px var(--brown-ink);
    text-shadow: 2px 2px 0 var(--brown-ink);
    line-height: 1;
  }
  .day-label { left: 27px; top: 250px; font-size: 38px; }
  .happy-hour { left: 27px; top: 300px; font-size: 104px; transform: rotate(-2deg); }
  .happy-time { left: 27px; top: 424px; font-size: 30px; font-weight: 900; color: var(--white); }
  .happy-offer { left: 195px; top: 422px; font-family: "Bungee Inline", sans-serif; font-size: 33px; color: var(--cream); text-shadow: 2px 2px 0 #222; }

  .poker-day { left: 132px; top: 508px; font-size: 36px; }
  .poker-title { left: 327px; top: 530px; font-size: 106px; transform: rotate(-3deg); }
  .poker-money { left: 448px; top: 656px; font-family: "Alfa Slab One", serif; font-size: 56px; color: var(--gold); text-shadow: 2px 2px 0 #5a3c08; }
  .poker-prizes { left: 585px; top: 668px; font-size: 44px; color: var(--white); -webkit-text-stroke: 1px #222; text-shadow: 2px 2px 0 #222; }

  .everyday { left: 18px; top: 676px; font-size: 36px; color: var(--cream); }
  .price-badge { left: 235px; top: 648px; width: 140px; height: 140px; }

  .chalkboard {
    left: 0; top: 732px; width: 307px; height: 228px;
    background: var(--board); border: 12px solid var(--board-frame); border-left: none;
    box-shadow: 4px 6px 10px rgba(0,0,0,.45);
    font-family: "Schoolbell", cursive; color: #f4f4f4;
  }
  .chalk-title { position: absolute; left: 24px; top: 22px; font-size: 34px; line-height: 1.05; }
  .chalk-title .indent { padding-left: 54px; display: block; }
  .chalk-note { position: absolute; left: 24px; top: 120px; font-size: 17px; line-height: 1.4; }

  .sports { left: 27px; top: 982px; font-size: 30px; font-weight: 900; color: var(--white); text-shadow: 2px 2px 0 #222; }
  .big-screen { left: 226px; top: 1018px; font-family: "Kaushan Script", cursive; font-size: 30px; color: var(--yellow); text-shadow: 2px 2px 0 #222; }

  .bistro-panel { left: 387px; top: 762px; width: 462px; height: 250px; background: var(--maroon); }
  .bistro-title { left: 607px; top: 772px; font-size: 68px; color: #e8b6e4; }
  .bistro-hours { left: 395px; top: 874px; font-family: "Mystery Quest", cursive; font-size: 44px; color: var(--cream); text-shadow: 2px 2px 0 var(--brown-ink); }
  .bistro-line { left: 395px; font-family: "Mystery Quest", cursive; font-size: 30px; color: var(--cream); text-shadow: 2px 2px 0 var(--brown-ink); width: 440px; text-align: center; }
  .bistro-specials { top: 924px; }
  .bistro-menu { top: 958px; }

  .footer-band {
    left: 0; top: 1095px; width: 849px; height: 105px;
    background: linear-gradient(180deg, var(--wood-light), var(--wood-dark));
    display: flex; align-items: center; justify-content: center;
  }
  .footer-text { font-family: "Alfa Slab One", serif; font-size: 58px; color: var(--silver); letter-spacing: 2px; text-shadow: 3px 3px 0 #1e120a; }
</style>
</head>
<body>
<main class="poster">
  <div class="abs brand-panel"></div>
  <div class="abs brand-name">Carrowfield Hotel</div>

  <svg class="abs open-sign" viewBox="0 0 364 280" aria-label="Open 9am to 3am, 7 days">
    <line x1="175" y1="10" x2="28" y2="70" stroke="#d8d8d8" stroke-width="3"/>
    <line x1="175" y1="10" x2="336" y2="86" stroke="#d8d8d8" stroke-width="3"/>
    <circle cx="175" cy="10" r="8" fill="#e8e8e8"/>
    <g transform="rotate(4 180 170)">
      <rect x="14" y="62" width="330" height="200" rx="14" fill="var(--sign-edge)"/>
      <rect x="26" y="74" width="306" height="176" rx="8" fill="var(--sign-fill)"/>
      <text x="179" y="125" text-anchor="middle" font-family="Roboto, sans-serif" font-weight="900" font-size="42" fill="#fff">OPEN</text>
      <text x="179" y="172" text-anchor="middle" font-family="Roboto, sans-serif" font-weight="700" font-size="35" fill="#fff">9am - 3am</text>
      <text x="179" y="218" text-anchor="middle" font-family="Roboto, sans-serif" font-weight="700" font-size="35" fill="#fff">7 days</text>
    </g>
  </svg>

  <div class="abs script-label day-label">Monday - Thursday</div>
  <div class="abs script-heading happy-hour">Happy Hour</div>
  <div class="abs happy-time">4pm - 6pm</div>
  <div class="abs happy-offer">LOCAL BEER &amp; WINE</div>

  <div class="abs script-label poker-day">Wednesday's</div>
  <div class="abs script-heading poker-title">Poker night</div>
  <div class="abs poker-money">$$$</div>
  <div class="abs script-label poker-prizes">Great prizes</div>

  <div class="abs script-label everyday">Everyday</div>
  <svg class="abs price-badge" viewBox="0 0 140 140" aria-label="$8.50">
    <polygon fill="var(--badge-blue)" points="70,2 79,22 97,8 99,30 121,24 114,45 136,50 120,66 138,80 116,87 126,107 104,106 104,128 85,118 77,139 66,120 51,136 46,114 25,122 30,100 8,95 24,79 4,66 24,56 12,36 34,36 32,13 52,24"/>
    <text x="70" y="80" text-anchor="middle" font-family="Roboto, sans-serif" font-weight="900" font-size="30" fill="#fff">$8.50</text>
  </svg>

  <div class="abs chalkboard">
    <div class="chalk-title">Steak or<span class="indent">Schniztels</span></div>
    <div class="chalk-note">Served with<br>Mashed Potato &amp; Salad or<br>Chips &amp; Salad</div>
  </div>

  <div class="abs sports">+ live sports on</div>
  <div class="abs big-screen">Big Screen</div>

  <div class="abs bistro-panel"></div>
  <div class="abs script-heading bistro-title">Bistro</div>
  <div class="abs bistro-hours">Open 7 days 12 - 9pm</div>
  <div class="abs bistro-line bistro-specials">Daily Blackboard Specials</div>
  <div class="abs bistro-line bistro-menu">+ Full Menu Inside</div>

  <div class="abs footer-band"><span class="footer-text">BEST SERVICE IN TOWN</span></div>
</main>
</body>
</html>
```